Commercial Flooring Contractor Website ($100 Bonus)

We are working with a new commercial flooring contractor in California. They work on schools, hospitals, and government projects.
A few websites for inspiration:
https://trimcoverwork.example (These guys are competitors and provide the same work our client does).
https://zqpavingsco.example (Although NOT a contractor, the simplicity of this site is stunning).
https://www.quietrapid.example (NOT a flooring contractor, but this site is modern, and has a boldness to it).
https://www.dawnfoldatelier.example/en-us (website for an Architectural office that is clean and showcases their work. I can see this working for a flooring contractor).
Thank you for taking the time to consider designing a website for us. We are web developers based in Stockton, CA, USA. Most of our projects go through the same process. Understanding this process may help you win a project with us. We custom-code all of our websites in-house. We don’t have any requirements as to what tools you use for your design, but we ask that you follow these guidelines.
IMAGES:
If you use any images or icons in the design, we ask that you have a link to the asset so we can purchase the image/icon. Most of the designs we submit do not have the customer’s images on them unless they have some great images. Be creative; show us the feeling you are trying to portray with your image choices. Use any royalty-free site you choose. We subscribe to Velto and mainly use their images, but we can purchase images outside of Velto.
FONTS:
We ask that you identify the fonts you’re using in the design. This can be done in a message if you want. We typically use Google Fonts and Velto Fonts.
CONTENT:
We're always open to different content and ideas. We often submit designs with stock images so the client can see our vision. We typically take pictures after the website launch to use their images with our vision. Lorem Ipsum is fine for paragraphs, but we ask that you make the Headers with correct English. We want to be able to show the vision and identify the sections of the website.
INSPIRATION:
We typically add a couple of links in the brief of websites we like to help you get started in your design.
REVISIONS:
We do not often ask for revisions of the designs unless we see something in the design that may not appeal to the client. If there are slight changes that we want to make, we do that in the development process.
FEEDBACK:
We rarely give feedback on designs during the design process. We are working on many website projects and do not have the time to provide feedback. We usually respond if your request is well thought out and asks specific questions, but a note asking “feedback, please” usually goes unanswered.
1 page

```html
<!DOCTYPE html>
<html lang="en">
<head>
<meta charset="utf-8">
<title>Corniche Floors — Commercial Flooring Services</title>
<link href="https://fonts.googleapis.com/css2?family=Bebas+Neue&family=Poppins:wght@400;500;600;700&display=swap" rel="stylesheet">
<style>
:root{
  --red:#e8343b;
  --red-dark:#d42a31;
  --ink:#1d1d1f;
  --text:#555;
  --muted:#888;
  --light:#f4f4f5;
  --dark:#141414;
  --white:#fff;
  --wood:#b98a62;
  --wood-deep:#8f6440;
}
*{box-sizing:border-box;margin:0;padding:0}
html,body{width:1200px;height:5098px;overflow:hidden}
body{position:relative;font-family:"Poppins",sans-serif;color:var(--text);background:var(--white)}
.abs{position:absolute}
.display{font-family:"Bebas Neue",sans-serif;color:var(--ink);letter-spacing:.5px;line-height:1.2}
.eyebrow{font-family:"Bebas Neue",sans-serif;color:var(--red);font-size:13px;letter-spacing:.5px}
.btn{position:absolute;background:var(--red);color:var(--white);font-size:11px;font-weight:600;text-transform:uppercase;display:flex;align-items:center;justify-content:center;letter-spacing:.3px}
.photo{position:absolute}

/* top bar */
.topbar{left:535px;top:0;width:665px;height:44px;background:var(--dark);display:flex;align-items:center;color:var(--white);font-size:11px;font-weight:500;gap:0;padding-left:58px}
.topbar .social{display:flex;gap:8px;margin-right:48px}
.topbar .social span{width:16px;height:16px;border-radius:50%;border:2px solid var(--white)}
.topbar .item{display:flex;align-items:center;gap:10px;margin-right:70px}
.brand{left:142px;top:10px;width:120px;height:92px;display:flex;align-items:center;gap:6px}
.brand .dot{width:14px;height:14px;border-radius:50%;background:var(--red);flex:none}
.brand .name{font-family:"Bebas Neue",sans-serif;font-size:26px;color:var(--ink);line-height:.95}
.nav{left:372px;top:76px;display:flex;gap:32px;font-size:11px;font-weight:600;color:var(--ink);text-transform:uppercase}
.nav .active{color:var(--red)}
.nav-cta{left:880px;top:63px;width:174px;height:40px}

/* hero */
.hero{left:0;top:116px;width:1200px;height:640px;background:linear-gradient(180deg,#2d3440 0%,#414650 38%,#6a4a33 62%,#9a6c45 100%)}
.hero-title{left:0;top:205px;width:1200px;text-align:center;color:var(--white);font-size:52px;line-height:60px}
.hero-list{left:0;top:350px;width:1200px;display:flex;justify-content:center;gap:26px;color:var(--white);font-family:"Bebas Neue",sans-serif;font-size:19px}
.hero-list span{display:flex;align-items:center;gap:8px}
.hero-cta{left:513px;top:405px;width:175px;height:40px}
.dots{left:98px;top:340px;display:flex;flex-direction:column;gap:22px;align-items:center}
.dots span{width:6px;height:6px;border-radius:50%;background:rgba(255,255,255,.7)}
.dots .on{width:18px;height:18px;border:2px solid var(--white);background:radial-gradient(var(--red) 35%,transparent 40%)}
.play{left:1082px;top:343px;width:48px;height:48px;border-radius:50%;background:rgba(255,255,255,.9);display:flex;align-items:center;justify-content:center}
.mouse{left:576px;top:692px;width:48px;height:48px;border-radius:50%;background:rgba(0,0,0,.35);display:flex;align-items:center;justify-content:center}

/* about */
.about-head{left:608px;top:896px;font-size:27px;line-height:39px}
.about-body{left:610px;top:990px;width:430px;font-size:11px;line-height:22px}
.dotgrid{left:332px;top:1400px;width:140px;height:90px;background-image:radial-gradient(#c9c9c9 1.3px,transparent 1.6px);background-size:12px 12px}

/* services */
.services-bg{left:0;top:1575px;width:1200px;height:1040px;background:var(--light)}
.card{position:absolute;width:292px;height:325px;overflow:hidden}
.card .label{position:absolute;right:34px;bottom:34px;color:var(--white);font-family:"Bebas Neue",sans-serif;font-size:28px;display:flex;gap:14px;align-items:center}
.card .corner{position:absolute;right:14px;bottom:14px;width:44px;height:44px;border-right:1px solid rgba(255,255,255,.8);border-bottom:1px solid rgba(255,255,255,.8)}
.card .tl{position:absolute;left:14px;top:14px;width:44px;height:44px;border-left:1px solid rgba(255,255,255,.8);border-top:1px solid rgba(255,255,255,.8)}

/* contact */
.contact-title{left:142px;top:3566px;color:var(--white);font-size:28px;line-height:38px}
.field{position:absolute;background:var(--white);font-size:10px;color:#777;padding:0 16px;display:flex;align-items:center;justify-content:space-between}

/* testimonials */
.t-card{position:absolute;top:4300px;width:300px;height:230px;background:var(--white);text-align:center;box-shadow:0 8px 30px rgba(0,0,0,.06)}
.t-avatar{position:absolute;left:115px;top:-30px;width:70px;height:70px;border-radius:50%;background:linear-gradient(160deg,#c9b6a4,#6d5a4d);border:3px solid var(--white)}
.t-card .who{margin-top:52px;font-size:12px;font-weight:600;color:var(--ink)}
.t-card .role{font-size:9px;color:var(--muted);margin-top:2px}
.t-card p{font-size:10.5px;line-height:21px;margin:10px 30px 6px}
.stars{color:var(--red);font-size:15px;letter-spacing:3px}

/* footer */
.footer{left:0;top:4660px;width:1200px;height:438px;background:var(--dark)}
.f-col{position:absolute;top:4904px;width:300px;text-align:center;color:#ccc;font-size:11px}
.f-col h4{font-family:"Bebas Neue",sans-serif;color:var(--white);font-size:17px;font-weight:400;margin-bottom:18px;letter-spacing:.5px}
.f-social{left:552px;top:5010px;display:flex;gap:10px}
.f-social span{width:24px;height:24px;border-radius:50%;border:2px solid #ccc}
</style>
</head>
<body>

<!-- header -->
<div class="abs topbar">
  <div class="social"><span></span><span></span><span></span></div>
  <div class="item">
    <svg width="12" height="15" viewBox="0 0 12 15"><path d="M6 0a6 6 0 0 0-6 6c0 4.5 6 9 6 9s6-4.5 6-9a6 6 0 0 0-6-6zm0 8.3A2.3 2.3 0 1 1 6 3.7a2.3 2.3 0 0 1 0 4.6z" fill="#fff"/></svg>
    AREAS WE SERVE</div>
  <div class="item">
    <svg width="13" height="13" viewBox="0 0 24 24"><path d="M6.6 10.8a15 15 0 0 0 6.6 6.6l2.2-2.2a1 1 0 0 1 1-.25 11.4 11.4 0 0 0 3.6.57 1 1 0 0 1 1 1V20a1 1 0 0 1-1 1A17 17 0 0 1 3 4a1 1 0 0 1 1-1h3.5a1 1 0 0 1 1 1c0 1.25.2 2.45.57 3.57a1 1 0 0 1-.25 1z" fill="#fff"/></svg>
    CALL US : 555 014 2290</div>
</div>
<div class="abs brand"><span class="dot"></span><span class="name">Corniche<br>Floors</span></div>
<nav class="abs nav">
  <span class="active">Home</span><span>About Us</span><span>Our Services</span><span>Latest Projects</span><span>Contact Us</span>
</nav>
<div class="btn nav-cta">Free Consulatation</div>

<!-- hero -->
<div class="abs hero" role="img" aria-label="Photo of a modern boardroom with a long table, black chairs, wood plank floor and a city skyline through the windows"></div>
<svg class="abs" style="left:0;top:690px" width="1200" height="80" viewBox="0 0 1200 80"><path d="M0 45 C250 70 420 50 600 25 C780 0 950 25 1200 55 L1200 80 L0 80Z" fill="var(--red)"/><path d="M0 55 C250 80 420 60 600 36 C780 12 950 35 1200 66 L1200 80 L0 80Z" fill="#fff"/></svg>
<div class="abs display hero-title">We Provide Ultimate<br>Commercial Flooring Services.</div>
<div class="abs hero-list">
  <span><svg width="13" height="13"><circle cx="6.5" cy="6.5" r="6.5" fill="#fff"/><path d="M3.5 6.7l2 2 4-4" stroke="#333" stroke-width="1.6" fill="none"/></svg>Carpet</span>
  <span><svg width="13" height="13"><circle cx="6.5" cy="6.5" r="6.5" fill="#fff"/><path d="M3.5 6.7l2 2 4-4" stroke="#333" stroke-width="1.6" fill="none"/></svg>Wood</span>
  <span><svg width="13" height="13"><circle cx="6.5" cy="6.5" r="6.5" fill="#fff"/><path d="M3.5 6.7l2 2 4-4" stroke="#333" stroke-width="1.6" fill="none"/></svg>Tile</span>
  <span><svg width="13" height="13"><circle cx="6.5" cy="6.5" r="6.5" fill="#fff"/><path d="M3.5 6.7l2 2 4-4" stroke="#333" stroke-width="1.6" fill="none"/></svg>Laminate</span>
  <span><svg width="13" height="13"><circle cx="6.5" cy="6.5" r="6.5" fill="#fff"/><path d="M3.5 6.7l2 2 4-4" stroke="#333" stroke-width="1.6" fill="none"/></svg>Vinyl</span>
</div>
<div class="btn hero-cta">Free Consulatation</div>
<div class="abs dots"><span></span><span class="on"></span><span></span><span></span></div>
<div class="abs play"><svg width="14" height="16"><path d="M0 0l14 8-14 8z" fill="var(--red)"/></svg></div>
<div class="abs mouse"><svg width="12" height="20"><rect x="1" y="1" width="10" height="18" rx="5" stroke="#fff" fill="none" stroke-width="1.5"/><line x1="6" y1="5" x2="6" y2="9" stroke="#fff" stroke-width="1.5"/></svg></div>

<!-- about -->
<div class="photo" style="left:122px;top:855px;width:445px;height:543px;background:linear-gradient(150deg,#7b7873 0%,#a18a72 55%,#c7a684 100%)" role="img" aria-label="Photo of an installer in gloves fitting wood laminate planks with a mallet"></div>
<div class="dotgrid abs"></div>
<div class="photo" style="left:478px;top:1175px;width:577px;height:343px;background:linear-gradient(180deg,#2a2a2c 0%,#3b3b3d 45%,#8b6446 70%,#b48458 100%);border:5px solid #fff" role="img" aria-label="Photo of an empty office with dark walls, a skyline mural and wood flooring"></div>
<div class="abs eyebrow" style="left:608px;top:858px">About Us</div>
<div class="abs display about-head">We Provide The Best<br>Commercial Flooring Services</div>
<p class="abs about-body">We Are ROOFING the simply dummy text of the printing and typesetting industry. Lorem Ipsum has been the industry's standard dummy text ever since the 1500s, when an unknown printer took a galley of type and scrambled it to make. Sed ut perspiciatis unde omnis iste natus error sit voluptatem accusantium doloremque laudantium,We Are solar the simply dummy text of the printing and typesetting industry.</p>

<!-- services -->
<div class="abs services-bg"></div>
<svg class="abs" style="left:0;top:1560px" width="1200" height="40" viewBox="0 0 1200 40"><path d="M0 20 C300 0 500 35 800 20 C1000 10 1100 10 1200 18 L1200 40 L0 40Z" fill="var(--light)"/></svg>
<div class="abs eyebrow" style="left:0;top:1675px;width:1200px;text-align:center">Our Services</div>
<div class="abs display" style="left:0;top:1698px;width:1200px;text-align:center;font-size:28px">We Provide Flooring Services</div>

<div class="card" style="left:145px;top:1778px;background:linear-gradient(180deg,#d9d6d0,#8e8a84 70%,#6f6c68)" role="img" aria-label="Photo of a long hotel corridor with patterned carpet and wood doors"><span class="tl"></span><span class="corner"></span><span class="label">Wood</span></div>
<div class="card" style="left:453px;top:1778px;background:linear-gradient(170deg,#c7b9a6,#7d5a3f 60%,#4d3626)" role="img" aria-label="Photo of a worker applying a floor coating to a wood floor with a roller"><span class="tl"></span><span class="corner"></span><span class="label">Coatings</span></div>
<div class="card" style="left:764px;top:1778px;background:linear-gradient(180deg,#d7dadb,#8f9396 55%,#4e5154)" role="img" aria-label="Photo of an office lounge with grey carpet tiles and orange seats"><span class="tl"></span><span class="corner"></span><span class="label">Carpet</span></div>
<div class="card" style="left:145px;top:2122px;background:linear-gradient(180deg,#3a3a3a,#b9b7b3 45%,#d9d7d2)" role="img" aria-label="Photo of a concrete floor between tall white columns"><span class="tl"></span><span class="corner"></span><span class="label">Concrete</span></div>
<div class="card" style="left:453px;top:2122px;background:linear-gradient(160deg,#ef5a5f,#e23a40)" role="img" aria-label="Photo of a tiled interior under a red overlay"><span class="tl"></span><span class="corner"></span><span class="label">Tile <svg width="22" height="12"><path d="M0 6h20M14 1l6 5-6 5" stroke="#fff" stroke-width="1.5" fill="none"/></svg></span></div>
<div class="card" style="left:764px;top:2122px;background:linear-gradient(180deg,#e9e9e7,#a9a8a4 55%,#3a3a3a)" role="img" aria-label="Photo of a bright office with resilient flooring and black chairs"><span class="tl"></span><span class="corner"></span><span class="label">Resilient</span></div>
<div class="btn" style="left:515px;top:2530px;width:172px;height:40px">View All Services</div>

<!-- projects -->
<div class="abs eyebrow" style="left:147px;top:2778px">Projects</div>
<div class="abs display" style="left:147px;top:2802px;font-size:28px">Our Latest Projects</div>
<p class="abs" style="left:149px;top:2855px;width:420px;font-size:11px;line-height:23px">We Are ROOFING the simply dummy text of the printing and typesetting industry. Lorem Ipsum has been the industry's standard dummy text ever since the 1500s, when an unknown printer took a galley of type and scrambled it to make industry.</p>
<div class="btn" style="left:149px;top:2943px;width:172px;height:40px">View All Projects</div>
<div class="photo" style="left:612px;top:2750px;width:210px;height:305px;background:linear-gradient(180deg,#eceded,#c9c9c7 55%,#b89a7b)" role="img" aria-label="Photo of a bright office with wood floor and floor-to-ceiling windows"></div>
<div class="photo" style="left:845px;top:2750px;width:210px;height:305px;background:linear-gradient(180deg,#5f574e,#8c7763 45%,#a7a5a4)" role="img" aria-label="Photo of a building lobby with striped stone flooring"></div>
<div class="photo" style="left:140px;top:3079px;width:210px;height:306px;background:linear-gradient(180deg,#efefef,#b5b5b5 60%,#6c6c6c)" role="img" aria-label="Photo of a reception area with grey carpet tiles"></div>
<div class="photo" style="left:374px;top:3079px;width:210px;height:306px;background:linear-gradient(180deg,#2e2c29,#7a6345 50%,#3a3a3c)" role="img" aria-label="Photo of a hotel hallway with dark carpet and wood doors"></div>
<div class="photo" style="left:610px;top:3079px;width:447px;height:306px;background:linear-gradient(180deg,#f1f1f0,#dedcd9 55%,#c29a74)" role="img" aria-label="Photo of an office lounge with grey sofas on a light wood floor"></div>

<!-- contact -->
<div class="photo" style="left:0;top:3420px;width:1200px;height:600px;background:linear-gradient(135deg,#c49a72 0%,var(--wood) 45%,var(--wood-deep) 100%)" role="img" aria-label="Photo of a wood plank floor with a rocking chair, camera and books"></div>
<svg class="abs" style="left:0;top:3410px" width="1200" height="80" viewBox="0 0 1200 80"><path d="M0 0H1200V30C1000 -5 800 60 560 20 C350 -10 200 50 0 40Z" fill="#fff"/></svg>
<svg class="abs" style="left:0;top:3950px" width="1200" height="80" viewBox="0 0 1200 80"><path d="M0 20 C250 70 500 60 700 40 C900 20 1050 45 1200 60 V80 H0Z" fill="#fff"/></svg>
<div class="abs eyebrow" style="left:142px;top:3540px;color:#fff;font-size:11px">Contact Form</div>
<div class="abs display contact-title">Find Your Recommendation<br>For Your Needs Here.</div>
<div class="field" style="left:143px;top:3676px;width:157px;height:40px">Name</div>
<div class="field" style="left:309px;top:3676px;width:153px;height:40px">Email address</div>
<div class="field" style="left:143px;top:3737px;width:319px;height:40px">Select your services <svg width="8" height="5"><path d="M0 0l4 4 4-4" stroke="#777" fill="none"/></svg></div>
<div class="field" style="left:143px;top:3797px;width:319px;height:62px;align-items:flex-start;padding-top:14px">Message</div>
<div class="btn" style="left:145px;top:3884px;width:158px;height:44px">Submit Now</div>

<!-- testimonials -->
<div class="abs eyebrow" style="left:0;top:4088px;width:1200px;text-align:center">Testimonials</div>
<div class="abs display" style="left:0;top:4113px;width:1200px;text-align:center;font-size:26px">What Our Statisfied Clients Are Saying</div>
<p class="abs" style="left:350px;top:4163px;width:500px;text-align:center;font-size:11px;line-height:23px">Lorem Ipsum has been the industry's standard dummy text ever since the 1500s, when an unknown printer took a galley of type and scrambled it to make</p>
<div class="t-card" style="left:146px"><span class="t-avatar" role="img" aria-label="Client portrait"></span><div class="who">Mara Kessel</div><div class="role">Customer</div><p>Lorem ipsum dolor sit amet nsectetur cing elit. Suspe ndisse suscipit sagittis leo sit met entum estibu dignissim posuere cubilia durae. Leo sauctor.</p><div class="stars">★★★★★</div></div>
<div class="t-card" style="left:450px"><span class="t-avatar" role="img" aria-label="Client portrait"></span><div class="who">Mara Kessel</div><div class="role">Customer</div><p>Lorem ipsum dolor sit amet nsectetur cing elit. Suspe ndisse suscipit sagittis leo sit met entum estibu dignissim posuere cubilia durae. Leo sauctor.</p><div class="stars">★★★★★</div></div>
<div class="t-card" style="left:773px"><span class="t-avatar" role="img" aria-label="Client portrait"></span><div class="who">Mara Kessel</div><div class="role">Customer</div><p>Lorem ipsum dolor sit amet nsectetur cing elit. Suspe ndisse suscipit sagittis leo sit met entum estibu dignissim posuere cubilia durae. Leo sauctor.</p><div class="stars">★★★★★</div></div>
<svg class="abs" style="left:575px;top:4572px" width="90" height="20"><circle cx="10" cy="10" r="3" fill="#bbb"/><circle cx="46" cy="10" r="8" fill="none" stroke="#f3b4b6"/><circle cx="46" cy="10" r="4" fill="var(--red)"/><circle cx="82" cy="10" r="3" fill="#bbb"/></svg>

<!-- footer -->
<div class="abs footer"></div>
<svg class="abs" style="left:0;top:4640px" width="1200" height="70" viewBox="0 0 1200 70"><path d="M0 0H1200V30C1000 55 800 20 600 30 C400 40 200 50 0 40Z" fill="var(--red)"/><path d="M0 0H1200V20C1000 45 800 10 600 20 C400 30 200 40 0 30Z" fill="#fff"/></svg>
<div class="abs" style="left:546px;top:4705px;width:110px;height:110px;border-radius:50%;background:#fff;display:flex;align-items:center;justify-content:center;text-align:center"><span style="font-family:'Bebas Neue',sans-serif;font-size:24px;color:var(--ink);line-height:.95">Corniche<br>Floors</span></div>
<p class="abs" style="left:340px;top:4838px;width:520px;text-align:center;color:#bbb;font-size:11px;line-height:23px">Lorem Ipsum has been the industry's standard dummy text ever since the 1500s, when an unknown printer took a galley of type and scrambled it to make</p>
<div class="f-col" style="left:145px"><h4>Write Us</h4>hello@cornichefloors.example</div>
<div class="f-col" style="left:454px"><h4>Address</h4>418 Alder Row Suite 6, Fresno, CA 93701</div>
<div class="f-col" style="left:780px"><h4>Contact Us</h4>+1 555-014-7732</div>
<div class="abs f-social"><span></span><span></span><span></span></div>
<div class="abs" style="left:0;top:5058px;width:1200px;text-align:center;color:#777;font-size:9px">© 2023 Corniche Floors. All Rights Reserved.</div>

</body>
</html>
```